Brenwick Drilling Inc. Business card design

Business card design for "Brenwick Drilling Inc. - Directional Drilling Services"

Address is:

Brenwick Drilling Inc.
512 - 73 Tolvane Crescent SW
Calgary, Alberta, Canada
T2K 4P8

Please incorporate the logo design into the card, thank you.

Target Market(s)

Oil & Gas and Drilling

Industry/Entity Type

Business

```html
<!DOCTYPE html>
<html lang="en">
<head>
<meta charset="UTF-8">
<title>Brenwick Drilling Inc. – Business Card</title>
<link href="https://fonts.googleapis.com/css2?family=Montserrat:wght@400;500;700;800&display=swap" rel="stylesheet">
<style>
  :root{
    --backdrop:#e9e6e2;
    --card-dark:#0b0b0b;
    --card-light:#ffffff;
    --accent-red:#d8262b;
    --ink-white:#ffffff;
    --ink-grey:#d9d9d9;
    --ink-black:#111111;
  }
  *{margin:0;padding:0;box-sizing:border-box}
  html,body{width:1200px;height:913px;overflow:hidden}
  body{
    background:var(--backdrop);
    font-family:"Montserrat",Arial,sans-serif;
    display:flex;align-items:center;justify-content:center;gap:60px;
  }
  .card{
    width:525px;height:300px;position:relative;overflow:hidden;
    box-shadow:0 10px 28px rgba(0,0,0,.22);
  }
  /* Front: dark contact side */
  .card--front{background:var(--card-dark);color:var(--ink-white)}
  .front-brand{
    position:absolute;left:20px;top:60px;width:220px;height:180px;
    display:flex;flex-direction:column;align-items:center;justify-content:center;gap:16px;
  }
  .front-brand .brand-dot{width:64px;height:64px;border-radius:50%;background:var(--ink-white)}
  .front-brand .brand-name{font-weight:700;font-size:15px;color:var(--ink-white);text-align:center;line-height:1.3;white-space:nowrap}
  .contact{position:absolute;left:260px;top:52px;font-size:12.5px;line-height:1.4}
  .contact .person{font-weight:800;font-size:17px;letter-spacing:.5px}
  .contact .role{color:var(--ink-grey);margin-bottom:12px}
  .contact .company{color:var(--accent-red);font-weight:700}
  .contact .address{color:var(--ink-grey);margin-bottom:14px}
  .contact ul{list-style:none}
  .contact li{display:flex;align-items:center;gap:8px;color:var(--ink-grey);margin-bottom:3px}
  .contact li svg{flex:none}
  /* Back: white brand side */
  .card--back{background:var(--card-light);display:flex;flex-direction:column;align-items:center;justify-content:center}
  .back-mark{width:58px;height:58px;border-radius:50%;background:var(--ink-black);margin-bottom:20px}
  .back-name{font-weight:800;font-size:27px;letter-spacing:1.5px;color:var(--ink-black)}
  .back-tagline{font-weight:500;font-size:11.5px;letter-spacing:4.2px;color:var(--ink-black);margin-top:4px}
</style>
</head>
<body>
  <section class="card card--front" aria-label="Business card front">
    <div class="front-brand">
      <span class="brand-dot"></span>
      <span class="brand-name">Brenwick Drilling Inc.</span>
    </div>
    <div class="contact">
      <p class="person">DANIEL ORRICK</p>
      <p class="role">Executive Manager</p>
      <p class="company">Brenwick Drilling Inc.</p>
      <p class="address">512 - 73 Tolvane Crescent SW<br>Calgary, Alberta, Canada<br>T2K 4P8</p>
      <ul>
        <li><svg width="12" height="12" viewBox="0 0 24 24"><path fill="var(--accent-red)" d="M6.6 10.8a15 15 0 0 0 6.6 6.6l2.2-2.2c.3-.3.7-.4 1-.2 1.1.4 2.3.6 3.6.6.6 0 1 .4 1 1V20c0 .6-.4 1-1 1A17 17 0 0 1 3 4c0-.6.4-1 1-1h3.5c.6 0 1 .4 1 1 0 1.3.2 2.5.6 3.6.1.3 0 .7-.2 1z"/></svg>+61 3 9004 2716</li>
        <li><svg width="12" height="12" viewBox="0 0 24 24"><rect x="6" y="2" width="12" height="20" rx="2" fill="var(--accent-red)"/><rect x="8" y="5" width="8" height="11" fill="var(--card-dark)"/></svg>+61 3 9712 4583</li>
        <li><svg width="12" height="12" viewBox="0 0 24 24"><rect x="2" y="5" width="20" height="14" rx="1" fill="var(--accent-red)"/><path d="M2 6l10 7 10-7" fill="none" stroke="var(--card-dark)" stroke-width="1.6"/></svg>daniel@brenwickdrilling.com</li>
      </ul>
    </div>
  </section>

  <section class="card card--back" aria-label="Business card back">
    <span class="back-mark"></span>
    <p class="back-name">BRENWICK DRILLING INC.</p>
    <p class="back-tagline">DIRECTIONAL DRILLING SERVICES</p>
  </section>
</body>
</html>
```